Private Learning Centre in Singapore needs a flyer design

We need a flyer design for our upcoming education fair and also able to use it for day to day purpose. The aim is to attract parents, students to enrol for classes by offering them free trial class/assessment. 2 sided flyer with the front page as the logo only and details on the other page. We would like to see a final design in blue, white and it should be curious and attractive enough not to allow customers to throw it away once they received it.

Education

```html
<!DOCTYPE html>
<html lang="en">
<head>
<meta charset="utf-8">
<title>Bright Grove Academy – Flyer Options</title>
<link rel="stylesheet" href="https://fonts.googleapis.com/css2?family=EB+Garamond:wght@400;500&family=PT+Sans:wght@400&display=swap">
<style>
  :root {
    --backdrop: #d8b98c;
    --blue: #3d5fb3;
    --blue-mid: #5a7fcc;
    --blue-deep: #2f4c9c;
    --blue-pale: #c3d3ef;
    --white: #ffffff;
    --divider: #f6efe4;
  }
  html, body { margin: 0; padding: 0; overflow: hidden; }
  .canvas {
    position: relative; width: 1200px; height: 1009px; overflow: hidden;
    background: var(--backdrop);
    font-family: "PT Sans", Arial, sans-serif;
  }
  .shapes { position: absolute; inset: 0; }
  .option-label { position: absolute; color: var(--white); font-size: 20px; }
  .brand-name {
    position: absolute; font-family: "EB Garamond", Georgia, serif; font-weight: 500;
    text-transform: uppercase; letter-spacing: 0.12em; text-align: center; line-height: 1.15;
  }
  .block { position: absolute; text-align: center; }
  .serif { font-family: "EB Garamond", Georgia, serif; }
  .justify { text-align: justify; text-align-last: center; }
  .contact { line-height: 1.35; }
  .social-square {
    display: inline-block; width: 0.9em; height: 0.9em; background: currentColor;
    vertical-align: -0.1em; margin-right: 3px;
  }
</style>
</head>
<body>
<div class="canvas">
  <svg class="shapes" width="1200" height="1009" viewBox="0 0 1200 1009">
    <!-- dividers -->
    <line x1="462" y1="48" x2="462" y2="985" stroke="var(--divider)" stroke-width="2"/>
    <line x1="505" y1="478" x2="1145" y2="478" stroke="var(--divider)" stroke-width="2"/>

    <!-- option 1 front -->
    <circle cx="236" cy="260" r="187" fill="var(--white)" stroke="var(--blue)" stroke-width="2"/>
    <circle cx="236" cy="165" r="26" fill="var(--blue)"/>
    <!-- option 1 back -->
    <circle cx="236" cy="717" r="187" fill="var(--blue)"/>
    <circle cx="236" cy="570" r="13" fill="var(--white)"/>

    <!-- option 2 card with offer -->
    <rect x="585" y="52" width="208" height="366" rx="24" fill="var(--blue)"/>
    <rect x="595" y="62" width="188" height="346" rx="17" fill="var(--white)"/>
    <circle cx="626" cy="92" r="14" fill="var(--blue)"/>
    <polygon points="540,92 580,112 575,160 548,140 556,118" fill="var(--blue)"/>
    <polygon points="800,172 836,178 820,200 838,224 796,215" fill="var(--blue)"/>
    <polygon points="566,126 800,140 803,186 569,172" fill="var(--blue-mid)"/>
    <!-- option 2 card front -->
    <rect x="915" y="50" width="226" height="362" rx="28" fill="var(--blue)"/>
    <rect x="926" y="61" width="204" height="340" rx="20" fill="var(--white)"/>
    <circle cx="1028" cy="250" r="20" fill="var(--blue)"/>
    <polygon points="874,180 914,150 918,208 888,212" fill="var(--blue)"/>
    <polygon points="1098,112 1150,110 1172,88 1178,150 1110,160" fill="var(--blue)"/>

    <!-- option 3 front ribbon -->
    <polygon points="560,552 825,608 825,652 560,596 585,574" fill="var(--blue-pale)"/>
    <polygon points="538,640 828,706 828,872 538,806" fill="var(--white)"/>
    <circle cx="685" cy="790" r="16" fill="var(--blue)"/>
    <polygon points="545,838 800,880 800,945 545,903" fill="var(--blue-pale)"/>
    <polygon points="590,925 800,945 640,985 600,965 625,950" fill="var(--blue-pale)"/>

    <!-- option 3 back ribbon -->
    <polygon points="935,522 1140,566 1140,612 945,570 965,545" fill="var(--blue-deep)"/>
    <polygon points="905,600 1140,560 1140,612 905,655" fill="var(--blue)"/>
    <line x1="905" y1="634" x2="960" y2="624" stroke="var(--white)" stroke-width="1.5"/>
    <line x1="1085" y1="600" x2="1138" y2="590" stroke="var(--white)" stroke-width="1.5"/>
    <circle cx="1020" cy="610" r="12" fill="var(--white)"/>
    <polygon points="880,705 1165,640 1165,790 880,866" fill="var(--blue-mid)"/>
    <polygon points="912,890 1140,842 1140,905 912,952" fill="var(--blue)"/>
    <polygon points="905,952 1120,932 1085,962 1118,990 940,992" fill="var(--blue)"/>
  </svg>

  <span class="option-label" style="left:21px;top:44px;">Option 1</span>
  <span class="option-label" style="left:507px;top:420px;">Option 2</span>
  <span class="option-label" style="left:507px;top:940px;">Option 3</span>

  <!-- option 1 front -->
  <div class="brand-name" style="left:76px;top:210px;width:320px;font-size:34px;color:var(--blue);">Bright Grove<br>Academy</div>

  <!-- option 1 back -->
  <div class="brand-name" style="left:176px;top:588px;width:120px;font-size:9px;color:var(--white);">Bright Grove Academy</div>
  <div class="block" style="left:86px;top:618px;width:300px;font-size:21px;color:var(--white);">Free Trial Class</div>
  <div class="block" style="left:86px;top:683px;width:300px;font-size:12.6px;line-height:15.7px;color:var(--white);">Bright Grove Academy is where you can develop academic and life skills. Our teachers are the heartbeat of the business. They inspire and nurture students, helping them surpass their expectations. We cover English, Mathematics and Science from Primary and Secondary Levels.</div>
  <div class="block contact" style="left:116px;top:815px;width:240px;font-size:10.5px;color:var(--white);">Bright Grove Academy<br>18 Harbour Lane S400118<br>6100 4275<br>hello@brightgroveacademy.com<br><span class="social-square"></span>/brightgroveacademy</div>

  <!-- option 2 offer card -->
  <div class="block serif" style="left:645px;top:91px;width:140px;font-size:14px;line-height:1;color:var(--blue);">Bright Grove<br>Academy</div>
  <div class="block serif" style="left:570px;top:139px;width:230px;font-size:24px;color:var(--white);transform:rotate(3deg);">Free Trial Class</div>
  <div class="block serif justify" style="left:604px;top:189px;width:164px;font-size:11.6px;line-height:14.7px;color:var(--blue);">Bright Grove Academy is where you can develop academic and life skills. Our teachers are the heartbeat of the business. They inspire and nurture students, helping them surpass their expectations. We cover English, Mathematics and Science from Primary and Secondary Levels.</div>
  <div class="block serif contact" style="left:610px;top:342px;width:150px;font-size:7.4px;line-height:1.25;color:var(--blue);">Bright Grove Academy<br>18 Harbour Lane S400118<br>6100 4275<br>hello@brightgroveacademy.com<br><span class="social-square"></span>/brightgroveacademy</div>
  <!-- option 2 front card -->
  <div class="brand-name" style="left:948px;top:188px;width:160px;font-size:13px;color:var(--blue);">Bright Grove Academy</div>

  <!-- option 3 front ribbon -->
  <div class="brand-name" style="left:573px;top:712px;width:220px;font-size:22px;color:var(--blue);transform:rotate(13deg);">Bright Grove<br>Academy</div>

  <!-- option 3 back ribbon -->
  <div class="brand-name" style="left:960px;top:582px;width:120px;font-size:7px;color:var(--white);transform:rotate(-10deg);">Bright Grove Academy</div>
  <div class="block" style="left:885px;top:705px;width:275px;font-size:13.5px;line-height:17px;color:var(--white);text-align:left;transform:rotate(-13deg);">Bright Grove Academy is where you can develop academic and life skills. Our teachers are the heartbeat of the business. They inspire and nurture students, helping them surpass their expectations. We cover English, Mathematics and Science from Primary and Secondary Levels.</div>
  <div class="block contact" style="left:935px;top:862px;width:190px;font-size:10px;color:var(--white);transform:rotate(-12deg);">Bright Grove Academy<br>18 Harbour Lane S400118<br>6100 4275<br>hello@brightgroveacademy.com</div>
  <div class="block" style="left:960px;top:948px;width:160px;font-size:11px;color:var(--white);transform:rotate(-5deg);"><span class="social-square"></span>/brightgroveacademy</div>
</div>
</body>
</html>
```